Plakat-Design für eine Budgetplanung für ein Kinderbuch
Das vorgeschlagene Poster war von Anfang an unser Favorit. Es zeichnet sich aus, durch ein ansprechendes, klares und kindgerechtes Design. Wir haben die ausgesprochen zuverlässige Arbeit und Kommunikation sehr geschätzt und hoffen auf weitere Zusammenarbeit.
Zielgruppe
Wir sind ein Verlag und bringen nächsten Monat zwei Kinder-/Jugendbücher mit dem Thema Finanzbildung heraus. Das Alter der Zielgruppe ist zwischen 8 und 13 Jahren. Zu den Büchern gehört ein hochwertiges Posterset aus drei Postern. In diesem Auftrag soll zunächst das erste Poster designed werden. Hier geht es darum eine kleine 'Budgetplanung' zu erstellen. In weiteren Aufträgen sollen auch Illustrationen aufgewertet und Designs für Websites erstellt werden.
Aufgabenstellung
Wir werden einige Bilder bereitstellen, die verarbeitet werden dürfen (es müssen nicht alle verwendet werden!). Es wäre schön, wenn das Posterdesign so ausgelegt wird, dass die Bilder gut in das Gesamtdesign passen. Die Bildqualität des Posters soll auf DINA2 optimiert sein. Weiterhin stellen wir einen 'Beispiel-Geldplan' zur Verfügung, der alle Texte enthält, die das Poster beinhalten soll. Das Design dieses Beispiel-Geldplans soll unberücksichtigt bleiben. Das Gesamtdesign soll hochwertig und kreativ sein.

```html
<!DOCTYPE html>
<html lang="de">
<head>
<meta charset="utf-8">
<title>Wie ich mir meine Träume erfülle</title>
<link rel="stylesheet" href="https://fonts.googleapis.com/css2?family=Patrick+Hand&family=Open+Sans:wght@400&display=swap">
<style>
  :root {
    --sun: #ece24a;
    --amber: #e9a24a;
    --meadow: #9cc05a;
    --paper: #ebe5d9;
    --paper-shade: #d9d1c2;
    --ink: #1d1d1d;
    --accent: #e8874a;
    --field: #f5f4f1;
  }
  * { margin: 0; padding: 0; box-sizing: border-box; }
  html, body { width: 862px; height: 1200px; overflow: hidden; background: #ffffff; }
  .poster {
    position: relative; width: 862px; height: 1200px; overflow: hidden;
    background:
      linear-gradient(180deg, rgba(236,226,74,0) 72%, rgba(156,192,90,0.95) 88%),
      linear-gradient(90deg, var(--amber) 0%, rgba(233,162,74,0) 30%),
      linear-gradient(180deg, var(--sun) 0%, #eed772 45%, #e9d27c 75%);
  }
  .sheet {
    position: absolute; left: 122px; top: 124px; width: 603px; height: 913px;
    background: radial-gradient(circle at 30% 20%, #f0ebe1, var(--paper) 55%, var(--paper-shade));
    box-shadow: 2px 3px 8px rgba(0,0,0,0.25);
  }
  .art { position: absolute; border-radius: 14px; }
  .art--banknote { left: 88px; top: 92px; width: 220px; height: 112px; background: linear-gradient(120deg, #8fd8b0, #d6f2dc); transform: rotate(-9deg); }
  .art--swing { left: 674px; top: 50px; width: 160px; height: 300px; background: linear-gradient(180deg, rgba(70,190,160,0.55), rgba(220,80,160,0.45)); }
  .art--euro { left: 82px; top: 432px; width: 118px; height: 198px; background: linear-gradient(180deg, rgba(240,120,60,0.75), rgba(240,140,70,0.45)); }
  .art--piggy { left: 64px; top: 877px; width: 344px; height: 261px; background: linear-gradient(160deg, rgba(180,210,70,0.6), rgba(240,170,180,0.75)); }
  .art--board { left: 630px; top: 960px; width: 155px; height: 178px; background: linear-gradient(180deg, rgba(250,240,210,0.8), rgba(90,170,230,0.6)); }

  .title, .label { position: absolute; font-family: "Patrick Hand", cursive; color: var(--ink); line-height: 1; white-space: nowrap; }
  .title { left: 186px; top: 132px; font-size: 37px; font-weight: 400; letter-spacing: 0.5px; }
  .label { left: 207px; font-size: 23px; }
  .sub { position: absolute; right: 355px; font-family: "Open Sans", sans-serif; font-size: 17px; color: var(--ink); line-height: 1; white-space: nowrap; }
  .entry { position: absolute; left: 516px; width: 152px; height: 35px; background: var(--field); box-shadow: 1px 2px 3px rgba(0,0,0,0.25); }
  .dots { position: absolute; left: 518px; width: 149px; border-bottom: 3px dotted var(--accent); }
  .arrow { position: absolute; overflow: visible; }
</style>
</head>
<body>
<main class="poster">
  <div class="sheet"></div>

  <div class="art art--banknote" role="img" aria-label="Illustration eines Fünf-Euro-Geldscheins mit Europakarte"></div>
  <div class="art art--swing" role="img" aria-label="Illustration bunter Fantasiefiguren auf Schaukel und Brett"></div>
  <div class="art art--euro" role="img" aria-label="Illustration einer orangen Fantasiefigur mit Eurozeichen"></div>
  <div class="art art--piggy" role="img" aria-label="Illustration eines Sparschweins mit bunten Fantasiefiguren und Münzwagen"></div>
  <div class="art art--board" role="img" aria-label="Illustration einer blauen Fantasiefigur an einer Tafel mit Formeln und Glühbirnen"></div>

  <h1 class="title">Wie ich mir meine Träume erfülle</h1>

  <svg class="arrow" width="862" height="1200" style="left:0;top:0" aria-hidden="true">
    <g fill="none" stroke="#e8874a" stroke-width="3" stroke-linecap="round" stroke-linejoin="round">
      <path d="M439 231 H503 M493 223 L503 231 L493 239"/>
      <path d="M407 405 L501 398 M490 391 L501 398 L492 406"/>
      <path d="M389 482 H499 M489 474 L499 482 L489 490"/>
      <path d="M450 617 H499 M489 609 L499 617 L489 625"/>
      <path d="M450 680 H499 M489 672 L499 680 L489 688"/>
      <path d="M450 740 H499 M489 732 L499 740 L489 748"/>
    </g>
  </svg>

  <p class="label" style="top:219px">Ich erhalte jeden Monat:</p>
  <div class="entry" style="top:217px"></div>
  <p class="sub" style="top:268px">Davon Taschengeld:</p>
  <div class="dots" style="top:278px"></div>
  <p class="sub" style="top:294px">Aus meinem Verdienst:</p>
  <div class="dots" style="top:304px"></div>
  <p class="sub" style="top:320px">Durch meine Investition:</p>
  <div class="dots" style="top:330px"></div>

  <p class="label" style="top:360px">Ich brauche jeden Monat (für</p>
  <p class="label" style="top:390px">Freizeit, Essen etc.):</p>
  <div class="entry" style="top:365px"></div>

  <p class="label" style="top:467px">Ich möchte sparen:</p>
  <div class="entry" style="top:464px"></div>
  <p class="sub" style="top:510px">Für Wunsch 1:</p>
  <div class="dots" style="top:520px"></div>
  <p class="sub" style="top:536px">Für Wunsch 2:</p>
  <div class="dots" style="top:546px"></div>
  <p class="sub" style="top:562px">Für Wunsch 3:</p>
  <div class="dots" style="top:572px"></div>

  <p class="label" style="top:602px">Ich möchte investieren:</p>
  <div class="entry" style="top:600px"></div>

  <p class="label" style="top:664px">Ich möchte spenden:</p>
  <div class="entry" style="top:660px"></div>

  <p class="label" style="top:725px">Wieviel ich schon gespart</p>
  <p class="label" style="top:753px">habe:</p>
  <div class="entry" style="top:721px"></div>

  <p class="label" style="top:811px">Meine Träume gehen in</p>
  <p class="label" style="top:842px">Erfüllung in:</p>

  <p class="sub" style="top:881px">Wunsch 1:</p>
  <div class="dots" style="top:891px"></div>
  <p class="sub" style="top:906px">Wunsch 2:</p>
  <div class="dots" style="top:916px"></div>
  <p class="sub" style="top:933px">Wunsch 3:</p>
  <div class="dots" style="top:943px"></div>
</main>
</body>
</html>
```